New signage for workshop frontage. Tarnell Welding & Repair is the company name. Looking for a cool font, metal fabrication is the trade. Also use TWAR as the logo

```html
<!DOCTYPE html>
<html lang="en">
<head>
<meta charset="utf-8">
<title>Tarnell Welding &amp; Repair — Workshop Sign</title>
<link rel="stylesheet" href="https://fonts.googleapis.com/css2?family=Roboto:ital,wght@0,700;1,700;1,900&display=swap">
<style>
  :root {
    --backdrop: #d9d9da;
    --paper: #ffffff;
    --brand-blue: #1a7dc6;
    --ink-dark: #1c1d20;
    --photo-dark: #2b2d30;
    --photo-steel: #8f9398;
    --text-light: #ffffff;
  }
  * { margin: 0; padding: 0; box-sizing: border-box; }
  html, body {
    width: 1199px; height: 1200px; overflow: hidden;
    background: var(--backdrop);
    font-family: "Roboto", Arial, sans-serif;
  }
  .sign {
    position: absolute; left: 200px; top: 66px;
    width: 800px; height: 1066px;
    background: var(--paper); overflow: hidden;
  }
  .side-panel {
    position: absolute; left: 551px; top: 0;
    width: 249px; height: 446px;
    background: var(--brand-blue);
  }
  .accent-bar-vertical {
    position: absolute; left: 535px; top: 0;
    width: 16px; height: 215px;
    background: var(--ink-dark);
  }
  .accent-bar-horizontal {
    position: absolute; left: 577px; top: 973px;
    width: 223px; height: 42px;
    background: var(--ink-dark);
  }
  .brand-name {
    position: absolute; left: 62px; top: 54px;
    font-weight: 700; font-size: 92px; line-height: 1;
    letter-spacing: 2px; color: var(--ink-dark);
  }
  .info-block {
    position: absolute; left: 0; top: 490px;
    width: 577px; height: 576px;
    background: var(--brand-blue);
  }
  .team-photo {
    position: absolute; left: 152px; top: 211px;
    width: 540px; height: 344px;
    background: linear-gradient(180deg, var(--photo-steel) 0%, #6f7378 38%, var(--photo-dark) 62%, #3a3c3f 100%);
  }
  .headline {
    position: absolute; left: 62px; top: 648px;
    color: var(--text-light); text-transform: uppercase;
  }
  .headline-lead {
    display: block; font-style: italic; font-weight: 900;
    font-size: 80px; line-height: 1; letter-spacing: 1px;
  }
  .headline-rest {
    display: block; font-weight: 700;
    font-size: 60px; line-height: 1.1; margin-top: 8px;
  }
  .divider {
    position: absolute; left: 62px; top: 922px;
    width: 222px; height: 9px; background: var(--text-light);
  }
  .phone {
    position: absolute; left: 58px; top: 962px;
    display: flex; align-items: center; gap: 12px;
    color: var(--text-light);
    font-style: italic; font-weight: 700; font-size: 54px; line-height: 1;
  }
  .phone-icon { width: 40px; height: 40px; }
</style>
</head>
<body>
  <main class="sign">
    <div class="side-panel"></div>
    <div class="accent-bar-vertical"></div>
    <div class="brand-name">TWAR</div>
    <div class="info-block"></div>
    <div class="team-photo" role="img" aria-label="Photo of three workers in hi-vis shirts standing in front of a large stainless steel machine"></div>
    <h1 class="headline">
      <span class="headline-lead">Tarnell</span>
      <span class="headline-rest">Welding &amp;<br>Repair</span>
    </h1>
    <div class="divider"></div>
    <div class="phone">
      <svg class="phone-icon" viewBox="0 0 40 40" aria-hidden="true">
        <circle cx="20" cy="20" r="17" fill="none" stroke="#fff" stroke-width="3"/>
        <path d="M13 11c2-1 3 0 4 2l1 3c0 1-1 2-2 3 1 3 3 5 6 6 1-1 2-2 3-2l3 1c2 1 3 2 2 4-1 2-3 3-5 2-6-2-11-7-13-13-1-2 0-5 1-6z" fill="#fff"/>
      </svg>
      <span>0400 555 182</span>
    </div>
    <div class="accent-bar-horizontal"></div>
  </main>
</body>
</html>
```